Design a cool print brochure for an NGO / Give your work a global impact!!

Hi,
I provide a full design brief (below, please scroll) and a mood board (attached) to help you visualize inside my head.. ;-)
I am also available to help and have worked many years in advertising; we will understand each other.
Objective:
To design an A4 folded in two presentation brochure for a non-profit consulting agency called Vantriq.
Vantriq works in sustainability and international development = working with NGO’s, governments and private sector on global issues such as global warming, education for all etc.
Strategy:
This document is a first step in developing a communication strategy. It will be distributed during a major international event called the Meridale Outreach Forum.
Objective:
The double objective of the brochure is:
a) to inform the recipient of what Vantriq is, in the shortest time possible.
b) to showcase relevant projects to demonstrate Vantriq experience and expertise.
Target:
Main target:
Existing Vantriq contacts, such as members of development organizations, NGOs, private sector foundations (CSR), regional networks and other development actors.
NB: the main target already has a certain awareness of Vantriq: we will try to minimize text to maximize visual impact and readability.
Secondary target:
Vantriq will also distribute the brochure to new prospects of interest during the Meridale Forum.
Timing:
We will need to finalize the design and have the files by June 1st to allow time for print before the event.
Content:
The document should be concise, highly readable (no clutter) and include:
1. text (that we will provide)
and
2. visual elements such as images, shapes and info-graphics (that is you).
NB: Vantriq does not have its own image bank; photos will be provided by you.
Format:
A4 folded in half - 4pp A5 - PORTRAIT FORMAT) with an impactful visual in the front, logo, title and headline (please see examples in the mood board attached).
Design elements:
Vantriq does not have yet a visual identity (please see: http://vantriq.org) so there is room for creativity and no graphic chart to follow.
The sector of consulting in international development is rather conservative but our intention is to be disruptive and create a “Wow” effect. We count on you for that!
Therefore, the design should be “structured”, “organized”, “uncluttered” but also “modern”, “impactful”, “highly visual” (think infographic or mind map to describe our services and projects).
Please, take the time to see the attached presentation: I give you guidelines and examples of what we want and what we like.
We are looking forward to seeing your work and I am available for comments, questions and support.
Thank you.
RK
Target Market(s)
The full brief is in the project description: please, scroll through it.
The target market is : our existing clients base, working in sustainable development (read: NGO and Allied Assembly people)
Industry/Entity Type
Ngo
Font styles to use
Requirements
Must have
- - Design and color elements: please, no black and white. Our company website is in black and white and without graphics; we want the brochure to break away from that and start creating our brand identity; so please, show us colors and desing elements (shapes, backgrounds, etc).
- You have a chance to showcase your talent in terms of visual identity: what lines, forms, layout and colors can you come up with and apply throughout the brochure and serve as the visual identity of Vantriq?
- The structure of the document should be:
- - Front cover: design elements + impacful photo (see mood board example attached) +our logo + this headline: "Collective action for sustainable development and impact"
- - Inside front: a graphic representation of "Our Services": such as core activity in the center circle and satellite circles for the services we offer.
- - Inside back:
- 1. Icons and text boxes for "Our projects"
- 2. A world map of the countries where we have worked. Full list of countries is here:
- http://vantriq.org/experience-1
- - Back cover: our contact + logos of partners.
- Our partners are listed here:
- Please use their original logos (ie, in color).
- The design we will select will serve as a basis for a graphic chart...so more work to come...word to the wise ;)
- Please check out our website vantriq.org to see what we do etc.
Nice to have
- Icons to reflect our services: what icons can you come up with to describe "training services", "building networks" or "program management"?
- I give examples in the mood board.
Should not have
- We are open to creativity and want to generate a "Wow" effect.
- Just note that the sector is rather conservative so flashy colors and cartoon like characters should be avoided. Think "earth, global change, Allied Assembly, climate" without going too green (it's overdone). ;-)
- Make us stand out in the NGO world
- Now you.

```html
<!DOCTYPE html>
<html lang="en">
<head>
<meta charset="utf-8">
<title>Vantriq brochure – outer spread</title>
<link rel="stylesheet" href="https://fonts.googleapis.com/css2?family=Bebas+Neue&family=Ubuntu:wght@500&family=Lato:wght@400;700&display=swap">
<style>
  :root {
    --teal: #2ab19d;
    --teal-deep: #23a08d;
    --orange: #ef7425;
    --orange-deep: #c9551a;
    --lime: #a9c646;
    --lime-text: #d6e07a;
    --ink: #1f3b4d;
    --paper: #ffffff;
    --band: rgba(255,255,255,0.28);
  }
  * { margin: 0; padding: 0; box-sizing: border-box; }
  html, body { width: 1200px; height: 848px; overflow: hidden; background: var(--paper); }
  .spread { position: relative; width: 1200px; height: 848px; font-family: "Lato", sans-serif; }

  /* back cover */
  .back-cover { position: absolute; left: 0; top: 0; width: 597px; height: 848px; background: var(--paper); }
  .section-head { position: absolute; left: 90px; width: 444px; display: flex; align-items: flex-end; gap: 8px; }
  .section-head .rule { flex: 1; border-bottom: 3px dashed var(--lime); margin-bottom: 9px; }
  .section-head h2 { font-family: "Bebas Neue", sans-serif; font-weight: 400; font-size: 28px; line-height: 1; color: var(--orange); letter-spacing: 0.3px; }
  .partners-head { top: 440px; }
  .contact-head { top: 702px; }

  .partners { position: absolute; left: 90px; top: 0; width: 444px; height: 848px; }
  .partner-row { position: absolute; left: 0; width: 444px; display: flex; align-items: center; justify-content: space-between; }
  .partner { display: flex; align-items: center; gap: 6px; font-weight: 700; font-size: 13px; color: var(--ink); line-height: 1.1; }
  .partner .mark { width: 22px; height: 22px; flex: none; }
  .mark.circle { border-radius: 50%; }
  .mark.teal { background: var(--teal); }
  .mark.orange { background: var(--orange); }
  .mark.lime { background: var(--lime); }
  .mark.ink { background: var(--ink); }
  .row-1 { top: 478px; height: 66px; }
  .row-2 { top: 566px; height: 44px; }
  .row-3 { top: 630px; height: 40px; }

  .contact { position: absolute; left: 234px; top: 738px; width: 300px; text-align: right; text-transform: uppercase; color: var(--ink); }
  .contact p { font-size: 7px; line-height: 8.4px; }
  .contact .lines { margin-top: 10px; font-weight: 700; font-size: 7.2px; line-height: 8.4px; }

  .foot-band { position: absolute; left: 90px; top: 806px; width: 444px; height: 42px; background: var(--orange); border-radius: 42px 42px 0 0; }

  /* front cover */
  .front-cover { position: absolute; left: 597px; top: 0; width: 603px; height: 848px; overflow: hidden; }
  .cover-photo { position: absolute; inset: 0; background: radial-gradient(ellipse at 55% 40%, #31bba7 0%, var(--teal) 55%, var(--teal-deep) 100%); }
  .photo-glow { position: absolute; left: 225px; top: 228px; width: 150px; height: 268px; border-radius: 50% 50% 40% 40%;
    background: radial-gradient(ellipse at 50% 35%, rgba(255,255,255,0.95) 0%, rgba(225,245,238,0.85) 35%, rgba(180,225,214,0.5) 65%, rgba(42,177,157,0) 100%); }
  .photo-warm { position: absolute; border-radius: 50%;
    background: radial-gradient(ellipse at 40% 35%, #ffb27a 0%, var(--orange) 45%, var(--orange-deep) 80%, rgba(35,160,141,0) 100%); }
  .warm-1 { left: 68px; top: 598px; width: 122px; height: 104px; }
  .warm-2 { left: 292px; top: 632px; width: 266px; height: 140px; }
  .cover-frame { position: absolute; left: 0; top: 0; width: 603px; height: 848px; }
  .brand { position: absolute; left: 381px; top: 256px; font-family: "Ubuntu", sans-serif; font-weight: 500; font-size: 64px; line-height: 1; color: var(--paper); letter-spacing: -1px; }
  .headline-band { position: absolute; left: 371px; top: 365px; width: 232px; height: 55px; background: var(--band); }
  .headline { position: absolute; right: 37px; top: 366px; text-align: right; font-family: "Bebas Neue", sans-serif; font-weight: 400; font-size: 21px; line-height: 17px; letter-spacing: 0.3px; }
  .headline .o { color: var(--orange); }
  .headline .g { color: var(--lime-text); }
</style>
</head>
<body>
<main class="spread">

  <section class="back-cover">
    <div class="section-head partners-head"><span class="rule"></span><h2>Our Partners</h2></div>

    <div class="partners">
      <div class="partner-row row-1">
        <div class="partner"><span class="mark circle teal"></span>Allied<br>Assembly</div>
        <div class="partner"><span class="mark ink"></span>Eurovale<br>Union</div>
        <div class="partner"><span class="mark circle lime"></span>Verdant<br>Pact</div>
        <div class="partner"><span class="mark ink"></span>Solmere Business<br>School</div>
      </div>
      <div class="partner-row row-2">
        <div class="partner"><span class="mark orange"></span>Civitas<br>Network</div>
        <div class="partner"><span class="mark ink"></span>Haldemar<br>Foundation</div>
        <div class="partner"><span class="mark circle lime"></span>Institute of Public<br>Governance</div>
      </div>
      <div class="partner-row row-3">
        <div class="partner"><span class="mark circle teal"></span>Cooperia</div>
        <div class="partner"><span class="mark ink"></span>Brenmoor College</div>
        <div class="partner"><span class="mark orange"></span>Kestrel Development Agency</div>
      </div>
    </div>

    <div class="section-head contact-head"><span class="rule"></span><h2>Contact Us</h2></div>

    <div class="contact">
      <p>We are based in different cities in Europe.<br>
      You can contact any of us directly in About Us.<br>
      Alternatively, for general inquiries, you can use the number<br>
      and/or email below.</p>
      <p class="lines">T: +34 611 408 293<br>E: info@vantriq.org</p>
    </div>

    <div class="foot-band"></div>
  </section>

  <section class="front-cover">
    <div class="cover-photo" role="img" aria-label="Photograph: a glowing white energy-saving bulb floating above a teal surface, with three glossy orange incandescent bulbs lying on the floor">
      <div class="photo-glow"></div>
      <div class="photo-warm warm-1"></div>
      <div class="photo-warm warm-2"></div>
    </div>
    <svg class="cover-frame" viewBox="0 0 603 848" aria-hidden="true">
      <path d="M291 233 H568 V490 H291" fill="none" stroke="#ffffff" stroke-width="1.6" stroke-dasharray="5 4"/>
    </svg>
    <div class="brand">vantriq</div>
    <div class="headline-band"></div>
    <h1 class="headline">
      <span class="o">Collective action</span><br>
      <span class="o">for</span> <span class="g">sustainable</span><br>
      <span class="g">development</span> <span class="o">and</span> <span class="g">impact</span>
    </h1>
  </section>

</main>
</body>
</html>
```